Industrial Laundry News Paper Add

We need a color add for 1/4 page newspaper using blue and white. We are an industrial laundry providing linen washing for condo rental companies. We can provide linen rental and wash customer-owned goods

```html
<!DOCTYPE html>
<html lang="en">
<head>
<meta charset="utf-8">
<title>Alpine Crest Services – Newspaper Ad</title>
<link rel="stylesheet" href="https://fonts.googleapis.com/css2?family=Montserrat:wght@300;400;500;600;700&display=swap">
<style>
  :root {
    --navy: #1f3585;
    --navy-deep: #141f66;
    --navy-light: #2a4aa6;
    --silver: #b9bcc6;
    --white: #ffffff;
    --stage: #5a5a5a;
    --photo-a: #d9dde3;
    --photo-b: #8fb2de;
  }
  * { box-sizing: border-box; margin: 0; padding: 0; }
  html, body { width: 1200px; height: 2400px; overflow: hidden; }
  body {
    background: linear-gradient(180deg, #6a6a6a 0%, var(--stage) 100%);
    font-family: "Montserrat", sans-serif;
    position: relative;
  }
  .ad {
    position: absolute;
    left: 50px; top: 488px;
    width: 951px; height: 1230px;
    transform: scale(1.1567);
    transform-origin: top left;
    background: var(--white);
    overflow: hidden;
    box-shadow: 0 14px 30px rgba(0,0,0,.45);
  }
  .ad__photo {
    position: absolute; left: 0; top: 240px; width: 951px; height: 600px;
    background: radial-gradient(ellipse at 52% 45%, var(--photo-b) 0%, #c9d6e6 35%, var(--photo-a) 70%, #b8bcc4 100%);
  }
  .ad__shapes { position: absolute; inset: 0; }
  .brand {
    position: absolute; left: 78px; top: 128px;
    width: 330px;
    display: flex; align-items: center; gap: 14px;
  }
  .brand__mark { width: 22px; height: 22px; border-radius: 50%; background: var(--navy); flex: none; }
  .brand__name {
    font-size: 32px; font-weight: 700; color: var(--navy);
    letter-spacing: .5px; line-height: 1.15;
  }
  .headline { position: absolute; left: 471px; top: 84px; color: var(--navy-deep); font-weight: 400; }
  .headline__lead { display: block; font-size: 40px; font-weight: 300; line-height: 1.3; }
  .headline__main { display: block; font-size: 40px; font-weight: 600; line-height: 1.3; }
  .services-title {
    position: absolute; left: 507px; top: 858px;
    font-size: 38px; color: var(--white); letter-spacing: 5px;
  }
  .services-title__light { font-weight: 300; }
  .services-title__bold { font-weight: 700; }
  .service-list { position: absolute; list-style: none; color: var(--white); font-weight: 300; font-size: 21px; }
  .service-list--left { left: 75px; top: 925px; }
  .service-list--left li { margin-bottom: 18px; padding-left: 24px; position: relative; line-height: 1.3; }
  .service-list--right { left: 507px; top: 925px; width: 400px; }
  .service-list--right li { margin-bottom: 10px; line-height: 1.45; padding-left: 26px; position: relative; }
  .service-list li::before { content: "✓"; position: absolute; left: 0; font-weight: 400; }
  .divider { position: absolute; left: 72px; top: 1075px; width: 808px; height: 1px; background: rgba(255,255,255,.55); }
  .contact { position: absolute; color: var(--white); font-style: normal; }
  .contact__row { display: flex; align-items: flex-start; gap: 10px; font-size: 18px; font-weight: 500; line-height: 1.3; }
  .contact--postal { left: 68px; top: 1103px; }
  .contact--postal .contact__row + .contact__row { margin-top: 14px; }
  .contact__icon { width: 14px; height: 16px; margin-top: 3px; flex: none; }
  .contact__rule { position: absolute; left: 469px; top: 1110px; width: 2px; height: 76px; background: var(--white); }
  .contact--direct { left: 538px; top: 1110px; }
  .phone { display: flex; align-items: center; gap: 12px; font-size: 38px; font-weight: 600; }
  .phone__icon { width: 34px; height: 34px; }
  .web { display: flex; align-items: center; gap: 12px; margin-top: 6px; font-size: 18px; font-weight: 500; }
  .web__icon { width: 20px; height: 20px; }
</style>
</head>
<body>
  <main class="ad">
    <div class="ad__photo" role="img" aria-label="Photo of a smiling laundry worker in a blue apron holding a stack of folded towels in front of industrial washing machines"></div>

    <svg class="ad__shapes" viewBox="0 0 951 1230" width="951" height="1230" aria-hidden="true">
      <defs>
        <linearGradient id="panelFill" x1="0" y1="0" x2="0" y2="1">
          <stop offset="0" stop-color="#2a46a0"/>
          <stop offset="1" stop-color="#1c2f80"/>
        </linearGradient>
      </defs>
      <path d="M0 0 H951 V260 C800 200 620 220 460 265 C300 310 150 320 0 250 Z" fill="var(--white)"/>
      <path d="M0 250 C150 320 300 310 460 265 C620 220 800 200 951 260 V330 C820 265 650 255 480 295 C320 335 150 335 0 300 Z" fill="var(--navy)"/>
      <path d="M0 785 C250 800 500 770 951 775 V820 C850 800 700 810 520 850 C330 890 150 880 0 830 Z" fill="var(--navy-deep)"/>
      <path d="M0 830 C150 880 330 890 520 850 C700 810 850 800 951 820 V1230 H0 Z" fill="url(#panelFill)"/>
      <path d="M0 826 C150 876 330 886 520 846 C700 806 850 796 951 816" fill="none" stroke="var(--silver)" stroke-width="5"/>
    </svg>

    <div class="brand">
      <span class="brand__mark"></span>
      <span class="brand__name">ALPINE CREST<br>SERVICES</span>
    </div>

    <h1 class="headline">
      <span class="headline__lead">The First Name</span>
      <span class="headline__main">In Industrial Laundry</span>
    </h1>

    <h2 class="services-title"><span class="services-title__light">OUR </span><span class="services-title__bold">SERVICES</span></h2>

    <ul class="service-list service-list--left">
      <li>Commercial Laundry</li>
      <li>Carpet Cleaning</li>
      <li>Housekeeping In Pine Hollow</li>
    </ul>
    <ul class="service-list service-list--right">
      <li>Linen washing for condo rental<br>companies</li>
      <li>Linen rental and wash customer<br>-owned goods</li>
    </ul>

    <div class="divider"></div>

    <address class="contact contact--postal">
      <div class="contact__row">
        <svg class="contact__icon" viewBox="0 0 14 16"><circle cx="7" cy="5" r="3.5" fill="none" stroke="#fff" stroke-width="1.5"/><path d="M7 8.5 V15 M3 15 H11" stroke="#fff" stroke-width="1.5"/></svg>
        <span>Granite Peak Partners, Inc.<br>Pine Hollow, CA 90000, USA</span>
      </div>
      <div class="contact__row">
        <svg class="contact__icon" viewBox="0 0 14 16"><rect x="1" y="4" width="12" height="9" fill="none" stroke="#fff" stroke-width="1.3"/><path d="M1 4 L7 9 L13 4" fill="none" stroke="#fff" stroke-width="1.3"/></svg>
        <span>info@alpinecrestservices.com</span>
      </div>
    </address>

    <div class="contact__rule"></div>

    <div class="contact contact--direct">
      <div class="phone">
        <svg class="phone__icon" viewBox="0 0 34 34"><circle cx="17" cy="17" r="15" fill="none" stroke="#fff" stroke-width="2.5"/><path d="M12 9 C10 11 10 15 13 19 C16 23 20 25 23 24 L24.5 21.5 L21 19.5 L19.5 21 C17.5 20 15 17.5 14 15.5 L15.5 14 L13.5 10 Z" fill="#fff"/></svg>
        <span>+1.5550123456</span>
      </div>
      <div class="web">
        <svg class="web__icon" viewBox="0 0 20 20"><circle cx="10" cy="10" r="8.5" fill="none" stroke="#fff" stroke-width="1.5"/><ellipse cx="10" cy="10" rx="3.8" ry="8.5" fill="none" stroke="#fff" stroke-width="1.3"/><path d="M1.5 10 H18.5" stroke="#fff" stroke-width="1.3"/></svg>
        <span>www.AlpineCrestServices.com</span>
      </div>
    </div>
  </main>
</body>
</html>
```